1 Page Bio, describing our Mission to buy multifamily properties in Colorado Springs.

I am uploading a sample of an associate who is doing a similar thing in Tampa Florida. I will also upload an attempt by my assistant to make the flyer and I will upload 3 pictures to use, along with another document that has text to add. I want to be able to edit the document pretty easily inside a google doc. thanks, I want it to look clean and professional.

```html
<!DOCTYPE html>
<html lang="en">
<head>
<meta charset="utf-8">
<title>Multifamily Investment Bio – Colorado Springs</title>
<link rel="stylesheet" href="https://fonts.googleapis.com/css2?family=Didact+Gothic&family=Montserrat:wght@600;700&display=swap">
<style>
  :root {
    --ribbon-blue: #5aaccd;
    --ribbon-shadow: #a3a3a3;
    --accent-blue: #4fa6cb;
    --ink: #2a2a2a;
    --paper: #f6f6f7;
    --haze: #dfe1e4;
    --photo-green: #5b6b55;
    --portrait-grey: #b9b9b9;
  }
  * { margin: 0; padding: 0; box-sizing: border-box; }
  html, body { width: 848px; height: 1200px; overflow: hidden; background: var(--paper); }
  .sheet {
    position: relative; width: 848px; height: 1200px; overflow: hidden;
    font-family: "Didact Gothic", "Century Gothic", sans-serif; color: var(--ink);
    background: var(--paper);
  }
  .backdrop {
    position: absolute; inset: 0;
    background:
      linear-gradient(180deg, #fbfbfb 0%, #f5f5f6 35%, #e3e5e8 55%, #e8e9eb 62%, #efeff1 80%, #f3f3f5 100%);
  }
  .ribbon { position: absolute; width: 232px; height: 76px; }
  .ribbon svg { position: absolute; inset: 0; }
  .ribbon-label {
    position: absolute; inset: 0; display: flex; align-items: center; justify-content: center;
    padding-left: 14px; padding-bottom: 6px;
    font-family: "Montserrat", sans-serif; font-weight: 600; font-size: 21px;
    letter-spacing: 1px; color: #fff;
  }
  .block-text { position: absolute; font-size: 16.5px; line-height: 21px; letter-spacing: 0.4px; }
  .block-text p { white-space: nowrap; }
  .indent { padding-left: 9px; }

  .team-title {
    position: absolute; left: 305px; top: 500px; width: 238px; text-align: center;
    font-family: "Montserrat", sans-serif; font-weight: 700; font-size: 44px; line-height: 44px;
    color: var(--accent-blue); border-bottom: 2px solid var(--accent-blue); padding-bottom: 2px;
  }
  .section-title {
    position: absolute; text-align: center;
    font-family: "Montserrat", sans-serif; font-weight: 600; font-size: 22px; line-height: 24px;
    letter-spacing: 5px; color: var(--accent-blue); border-bottom: 1.5px solid var(--accent-blue);
  }
  .principals { left: 336px; top: 555px; width: 182px; }
  .advisors { left: 345px; top: 942px; width: 158px; }
  .person-name {
    position: absolute; left: 29px; font-family: "Montserrat", sans-serif; font-weight: 600;
    font-size: 20px; letter-spacing: 0.5px; color: var(--accent-blue);
  }
  .bio { position: absolute; left: 54px; font-size: 16.5px; line-height: 20.5px; letter-spacing: 0.4px; }
  .bio li { list-style: none; white-space: nowrap; }
  .principal-photo {
    position: absolute; left: 593px; top: 658px; width: 220px; height: 220px; border-radius: 50%;
    border: 1.5px solid #333;
    background: radial-gradient(circle at 50% 30%, #c9d0cc 0%, #7f8d78 45%, var(--photo-green) 100%);
  }
  .advisor-photo {
    position: absolute; top: 988px; width: 160px; height: 160px; border: 1.5px solid #333;
    background: linear-gradient(180deg, #ffffff 0%, #e6e6e6 50%, var(--portrait-grey) 100%);
  }
  .advisor-name {
    position: absolute; top: 1156px; width: 160px; text-align: center;
    font-family: "Montserrat", sans-serif; font-weight: 600; font-size: 17px; letter-spacing: 0.5px;
    color: var(--accent-blue);
  }
</style>
</head>
<body>
<main class="sheet">
  <div class="backdrop" role="img" aria-label="Faded photo of a city skyline across the water"></div>

  <!-- Top row ribbons -->
  <div class="ribbon" style="left:37px; top:24px;">
    <svg viewBox="0 0 232 76" width="232" height="76"><polygon points="6,73 13,32 13,74" fill="var(--ribbon-shadow)"/><polygon points="13,8 213,0 213,73 13,73" fill="var(--ribbon-shadow)"/><polygon points="7,7 220,7 212,66 7,79" fill="var(--ribbon-blue)"/></svg>
    <span class="ribbon-label">THE MISSION</span>
  </div>
  <div class="ribbon" style="left:314px; top:24px;">
    <svg viewBox="0 0 232 76" width="232" height="76"><polygon points="6,73 13,32 13,74" fill="var(--ribbon-shadow)"/><polygon points="13,8 213,0 213,73 13,73" fill="var(--ribbon-shadow)"/><polygon points="7,7 220,7 212,66 7,79" fill="var(--ribbon-blue)"/></svg>
    <span class="ribbon-label">VALUES</span>
  </div>
  <div class="ribbon" style="left:591px; top:24px;">
    <svg viewBox="0 0 232 76" width="232" height="76"><polygon points="6,73 13,32 13,74" fill="var(--ribbon-shadow)"/><polygon points="13,8 213,0 213,73 13,73" fill="var(--ribbon-shadow)"/><polygon points="7,7 220,7 212,66 7,79" fill="var(--ribbon-blue)"/></svg>
    <span class="ribbon-label">THE PROCESS</span>
  </div>

  <div class="block-text" style="left:37px; top:128px;">
    <p>To create a family business</p><p>by purchasing Multifamily</p><p>Residences, one at a time.</p>
  </div>
  <div class="block-text" style="left:314px; top:128px;">
    <p>To provide a white glove</p><p>experience to all residences</p><p>with a clean, safe, and fun</p><p>environment.</p>
  </div>
  <div class="block-text" style="left:591px; top:128px;">
    <p>Buy right, manage right,</p><p>and finance right.</p>
  </div>

  <!-- Middle row ribbons -->
  <div class="ribbon" style="left:140px; top:236px;">
    <svg viewBox="0 0 232 76" width="232" height="76"><polygon points="6,73 13,32 13,74" fill="var(--ribbon-shadow)"/><polygon points="13,8 213,0 213,73 13,73" fill="var(--ribbon-shadow)"/><polygon points="7,7 220,7 212,66 7,79" fill="var(--ribbon-blue)"/></svg>
    <span class="ribbon-label">THE MARKET</span>
  </div>
  <div class="ribbon" style="left:487px; top:236px;">
    <svg viewBox="0 0 232 76" width="232" height="76"><polygon points="6,73 13,32 13,74" fill="var(--ribbon-shadow)"/><polygon points="13,8 213,0 213,73 13,73" fill="var(--ribbon-shadow)"/><polygon points="7,7 220,7 212,66 7,79" fill="var(--ribbon-blue)"/></svg>
    <span class="ribbon-label">THE TARGET</span>
  </div>

  <div class="block-text" style="left:82px; top:341px;">
    <p>Colorado Springs</p>
    <p>-Projected job growth of nearly 50%</p>
    <p>-Below average unemployment rates.</p>
    <p>-Above-average incomes.</p>
    <p>-Solid economy, military, aerospace,</p>
    <p class="indent">electronics industry, and tourism.</p>
  </div>
  <div class="block-text" style="left:464px; top:341px;">
    <p>B and C class assets located</p><p>in Colorado Springs or nearby</p><p>submarkets.</p>
  </div>

  <!-- Team -->
  <h1 class="team-title">THE TEAM</h1>
  <h2 class="section-title principals">PRINCIPALS</h2>

  <h3 class="person-name" style="top:596px;">RUSSELL TANDRY</h3>
  <ul class="bio" style="top:630px;">
    <li>-Licensed Colorado Real Estate Agent 18 years.</li>
    <li>-Broker-Owner of two Summit Key Realty Franchises 7 and 2 Years.</li>
    <li>-Real Estate investing for 5 years.</li>
    <li>-Member of Keystone Rental Academy.</li>
    <li>-Married 24 years to Marla, parenting 10 children together.</li>
    <li>-Appeared on Ben and Lou’s Apartment Hour podcast</li>
    <li class="indent">Episode 43</li>
    <li>-$2M portfolio.</li>
  </ul>

  <div class="principal-photo" role="img" aria-label="Photo of the two principals standing outdoors among pine trees"></div>

  <h3 class="person-name" style="top:811px;">GLEN TANDRY</h3>
  <ul class="bio" style="top:845px;">
    <li>Retired Electrical Engineer.</li>
    <li>-Active Real Estate Investor/Consultant.</li>
    <li>-Net worth over $4M</li>
    <li>-15 Grandchildren.</li>
  </ul>

  <h2 class="section-title advisors">ADVISORS</h2>

  <div class="advisor-photo" style="left:232px;" role="img" aria-label="Black and white portrait of advisor Owen Marsh"></div>
  <div class="advisor-photo" style="left:456px;" role="img" aria-label="Black and white portrait of advisor Neil Corbett"></div>
  <p class="advisor-name" style="left:232px;">Owen Marsh</p>
  <p class="advisor-name" style="left:456px;">Neil Corbett</p>
</main>
</body>
</html>
```